Property lawyer needs a website for new law firm Sydney

WHO AM I ?
I am a real estate development lawyer based in suburban Sydney Australia with over 14 years experience and have recently started my own law firm "Bramblewood Legal". The firm is just me (a female) at this stage. I need a website designed that is capable of being edited by me frequently (hoping this is easily done?!) and can be published with the domain name I own - www.bramblewoodlegal.com.au.
My areas of practice are:
* Property development (strata & community titling, due diligence, easements, by-laws and management statements, structuring etc)
* Conveyancing (sale and purchase of residential, commercial and retail property)
* General property law (caveats, transfers, related party transactions, easements, leases, powers of attorney etc).
WEBSITE REQUIREMENTS
I would like a website which conveys professionalism, has a fresh modern corporate look and is easy to navigate. The website will mostly be accessed by potential clients looking for information about me, my areas of practice and how to get in contact with me. My potential clients are corporate developers and individuals who are buying and selling property.
My logo for Bramblewood Legal (see attached) is simple, clean and professional looking. I would like the website to work with the logo without being too dark.
I haven't written all of the content yet, so please use filler text for everything and structure the menus as described above. The site will need to be capable of being updated and edited by me.
Other than that I will leave the design up to you.
Thanks and happy designing!
Target Market(s)
Professional developers and individuals buying and selling real estate
Industry/Entity Type
Real Estate
Coding
Coded - Design and coding required
Number of Pages Required
4 page
Requirements
Must have
- I would like a website which conveys professionalism, has a fresh modern corporate look and is easy to navigate. The website will mostly be accessed by potential clients looking for information about me, my areas of practice and how to get in contact with me. My potential clients are corporate developers and individuals who are buying and selling property.
- Please use my logo for Bramblewood Legal. I would like the website to work with the logo - the colours are a dark blue (C 100% M 50% B 50%) and grey (C10% B 40%). I don't want the website to be too dark though.
- I am thinking 4 pages. I would like links across the top of the page for "Practice Areas", "About us" and "Contact us" - these should lead to separate landing pages with the content to be inserted later.
- The contact page should contain space for a potential client to send an email enquiry to the following email address "enquiries@bramblewoodlegal.com.au". My contact details are set out in the attached letterhead (see attached).
- I would also like the home page to set out what my three Practice Areas are - Property Development; Conveyancing; General Property Law. Each area should have some filler text under it which will be completed later and a link to be able to take me to the "Practice Areas" page where more detail on each will be provided.
- Please select images that are relevant to my practice as a property lawyer. The photos you use will be the ones which I use so please choose wisely.
- I will need a link on the bottom of the home page showing that I am a member of "The Counsel Guild of NSW" (see attached logo).
- The bottom of each page should also include the following statement "Bramblewood Legal is a business name of Bramblewood Legal Pty Limited ACN 482 517 306, an incorporated legal practice regulated by the Legal Profession Act 2004. Liability limited by a scheme approved under the Professional Standards Legislation."
Nice to have
- Have attached an image of me (not the best) but at least its me. Consider whether to use on "About us" page
Should not have
- No images of gavels, scales of justice or law books.
- Images not to be too masculine
- Website not to be too dark

```html
<!DOCTYPE html>
<html lang="en">
<head>
<meta charset="utf-8">
<title>Bramblewood Legal</title>
<link rel="stylesheet" href="https://fonts.googleapis.com/css2?family=Open+Sans:ital,wght@0,400;0,600;0,700;1,400&display=swap">
<style>
  :root {
    --brand-blue: #0b3a72;
    --link-blue: #0d4a8a;
    --ink: #333333;
    --rule: #e2e2e2;
    --header-top: #fafafa;
    --header-bottom: #dcdcdc;
    --footer: #333333;
    --footer-line: #4a4a4a;
    --white: #ffffff;
  }
  * { margin: 0; padding: 0; box-sizing: border-box; }
  html, body { width: 786px; height: 1200px; overflow: hidden; }
  body { font-family: "Open Sans", Arial, sans-serif; color: var(--ink); background: var(--white); position: relative; }
  .abs { position: absolute; }

  .site-header { position: absolute; left: 0; top: 0; width: 786px; height: 57px;
    background: linear-gradient(var(--header-top), var(--header-bottom)); z-index: 2; }
  .brand { position: absolute; left: 65px; top: 0; width: 201px; height: 74px; background: #1e1e1e;
    color: var(--white); font-size: 16px; font-weight: 400; letter-spacing: 0.3px;
    display: flex; align-items: center; justify-content: center; text-transform: uppercase; }
  .main-nav a { position: absolute; top: 0; height: 57px; line-height: 57px; font-size: 10.5px;
    color: #222; text-decoration: none; font-weight: 400; }
  .main-nav .is-active { left: 266px; width: 43px; background: var(--brand-blue); color: var(--white); text-align: center; }
  .guild-link { position: absolute; left: 646px; top: 12px; display: flex; align-items: center; gap: 4px;
    text-decoration: none; color: #222; }
  .guild-link span { font-size: 5.5px; line-height: 6px; text-transform: uppercase; letter-spacing: 0.1px; }

  .hero { position: absolute; left: 0; top: 57px; width: 786px; height: 385px;
    background: radial-gradient(ellipse at 50% 55%, #e9e2dc 0%, #d9cfc7 25%, #a9b98f 55%, #6f9a4a 100%); }
  .hero-arrow { position: absolute; top: 166px; }
  .hero-dots { position: absolute; left: 373px; top: 352px; display: flex; gap: 3px; }
  .hero-dots span { width: 11px; height: 11px; border-radius: 50%; background: var(--white); }
  .hero-dots .on { background: var(--brand-blue); }
  .hero-shade { position: absolute; left: 0; top: 442px; width: 786px; height: 10px;
    background: linear-gradient(rgba(0,0,0,0.08), rgba(0,0,0,0)); }

  .section-title { font-size: 19px; font-weight: 400; color: #2b2b2b; }
  .practice-list { list-style: none; width: 203px; }
  .practice-list li { height: 23.5px; border-bottom: 1px solid var(--rule); font-size: 9px;
    font-style: italic; display: flex; align-items: center; gap: 8px; padding-left: 11px; color: #333; }
  .practice-list li:first-child { border-top: 1px solid var(--rule); }
  .practice-list li:last-child { border-bottom: none; }
  .bullet { width: 13px; height: 13px; border-radius: 50%; background: #3a3a3a; display: inline-flex;
    align-items: center; justify-content: center; }
  .date-tag { background: var(--brand-blue); color: var(--white); font-size: 8px; width: 66px; height: 23px;
    line-height: 23px; text-align: center; }
  .news-text { font-size: 9px; line-height: 11px; color: #444; width: 205px; }
  .more { font-size: 10px; color: #222; display: flex; align-items: center; gap: 5px; }
  .more i { width: 11px; height: 11px; background: #222; border-radius: 2px; display: inline-flex;
    align-items: center; justify-content: center; }

  .portrait { position: absolute; left: 302px; top: 478px; width: 131px; height: 140px;
    border: 2px solid #bdbdbd; background: linear-gradient(#e8e8e8, #cfcfcf); }
  .intro-title { font-size: 22px; font-weight: 600; color: var(--brand-blue); letter-spacing: 0.3px; }
  .intro-sub { font-size: 13px; color: #333; }
  .intro-lead { font-size: 10px; font-weight: 600; line-height: 12px; color: #333; width: 258px; }
  .intro-body { font-size: 8.6px; line-height: 11px; color: #555; width: 252px; }

  .solution h3 { font-size: 10px; font-weight: 600; color: var(--link-blue); }
  .solution p { font-size: 8.6px; line-height: 11px; color: #555; width: 170px; }

  .contact-band { position: absolute; left: 0; top: 938px; width: 786px; height: 6px; background: #e6e6e6; }
  .site-footer { position: absolute; left: 0; top: 944px; width: 786px; height: 256px; background: var(--footer); color: #f2f2f2; }
  .contact-title { position: absolute; top: 22px; width: 786px; text-align: center; font-size: 20px; font-weight: 400; }
  .contact-text { position: absolute; top: 62px; width: 786px; text-align: center; font-size: 9.6px; line-height: 12.5px; }
  .contact-line { position: absolute; font-size: 9.6px; }
  .drop-btn { position: absolute; left: 320px; top: 163px; width: 146px; height: 30px; background: var(--brand-blue);
    color: var(--white); font-size: 10px; text-align: center; line-height: 30px; }
  .footer-rule { position: absolute; left: 0; top: 208px; width: 786px; height: 4px; background: var(--footer-line); }
  .copyright { position: absolute; left: 65px; top: 218px; font-size: 8.5px; }
  .disclaimer { position: absolute; left: 65px; top: 231px; width: 500px; font-size: 6.6px; line-height: 8.5px; color: #cfcfcf; }
  .social { position: absolute; top: 224px; display: flex; align-items: center; justify-content: center; width: 22px; height: 22px; }
</style>
</head>
<body>

<header class="site-header">
  <div class="brand">Bramblewood Legal</div>
  <nav class="main-nav">
    <a class="is-active" href="#">HOME</a>
    <a style="left:326px" href="#">ABOUT US</a>
    <a style="left:400px" href="#">SERVICES</a>
    <a style="left:468px" href="#">CONTACTS US</a>
  </nav>
  <a class="guild-link" href="#">
    <svg width="30" height="33" viewBox="0 0 30 33" aria-hidden="true">
      <path d="M2 2 H28 V16 C28 25 15 31 15 31 C15 31 2 25 2 16 Z" fill="#222"/>
    </svg>
    <span>Member of<br>The Counsel Guild<br>of NSW</span>
  </a>
</header>

<section class="hero" role="img" aria-label="Woman holding a model house in her open hands, green grass behind">
  <svg class="hero-arrow" style="left:25px" width="20" height="36" viewBox="0 0 20 36"><path d="M17 2 L4 18 L17 34" stroke="#fff" stroke-width="5" fill="none"/></svg>
  <svg class="hero-arrow" style="left:741px" width="20" height="36" viewBox="0 0 20 36"><path d="M3 2 L16 18 L3 34" stroke="#fff" stroke-width="5" fill="none"/></svg>
  <div class="hero-dots"><span class="on"></span><span></span><span></span></div>
</section>
<div class="hero-shade"></div>

<h2 class="section-title abs" style="left:65px;top:472px">Our Practice</h2>
<svg class="abs" style="left:246px;top:482px" width="22" height="10" viewBox="0 0 22 10">
  <rect width="10" height="10" rx="2" fill="#333"/><path d="M2.5 6.5 L5 3.5 L7.5 6.5" stroke="#fff" fill="none"/>
  <rect x="12" width="10" height="10" rx="2" fill="#333"/><path d="M14.5 3.5 L17 6.5 L19.5 3.5" stroke="#fff" fill="none"/>
</svg>
<ul class="practice-list abs" style="left:65px;top:502px">
  <li><span class="bullet"><svg width="7" height="7" viewBox="0 0 7 7"><path d="M1 3.5 H6 M4 1.5 L6 3.5 L4 5.5" stroke="#fff" fill="none"/></svg></span>Property Development</li>
  <li><span class="bullet"><svg width="7" height="7" viewBox="0 0 7 7"><path d="M1 3.5 H6 M4 1.5 L6 3.5 L4 5.5" stroke="#fff" fill="none"/></svg></span>Conveyancing</li>
  <li><span class="bullet"><svg width="7" height="7" viewBox="0 0 7 7"><path d="M1 3.5 H6 M4 1.5 L6 3.5 L4 5.5" stroke="#fff" fill="none"/></svg></span>General Property Law</li>
  <li><span class="bullet"><svg width="7" height="7" viewBox="0 0 7 7"><path d="M1 3.5 H6 M4 1.5 L6 3.5 L4 5.5" stroke="#fff" fill="none"/></svg></span>Strata &amp; Community Title</li>
  <li><span class="bullet"><svg width="7" height="7" viewBox="0 0 7 7"><path d="M1 3.5 H6 M4 1.5 L6 3.5 L4 5.5" stroke="#fff" fill="none"/></svg></span>Due Diligence</li>
  <li><span class="bullet"><svg width="7" height="7" viewBox="0 0 7 7"><path d="M1 3.5 H6 M4 1.5 L6 3.5 L4 5.5" stroke="#fff" fill="none"/></svg></span>Leases &amp; Easements</li>
  <li><span class="bullet"><svg width="7" height="7" viewBox="0 0 7 7"><path d="M1 3.5 H6 M4 1.5 L6 3.5 L4 5.5" stroke="#fff" fill="none"/></svg></span>Powers of Attorney</li>
</ul>

<h2 class="section-title abs" style="left:65px;top:685px">News &amp; Events</h2>
<div class="date-tag abs" style="left:65px;top:729px">12/10/2015</div>
<p class="news-text abs" style="left:65px;top:763px">Wed est lab orum eunam libero tempore, cum soluta nobis est elienisa omnis voluptas assu-menda est, omnis doloresed repellendus</p>
<div class="date-tag abs" style="left:65px;top:820px">12/10/2015</div>
<p class="news-text abs" style="left:65px;top:855px">Wed est lab orum eunam libero tempore, cum soluta nobis est elienisa omnis voluptas assu-menda est, omnis doloresed repellendus</p>
<div class="more abs" style="left:65px;top:898px"><i><svg width="7" height="7" viewBox="0 0 7 7"><path d="M1 1 L3.5 3.5 L1 6 M3.5 1 L6 3.5 L3.5 6" stroke="#fff" fill="none"/></svg></i>archive</div>

<div class="portrait" role="img" aria-label="Portrait photo of the principal lawyer"></div>
<h1 class="intro-title abs" style="left:446px;top:477px">Need Practical Help ?</h1>
<p class="intro-sub abs" style="left:447px;top:512px">We hold the national quality standard.</p>
<p class="intro-lead abs" style="left:447px;top:541px">Lorem ipsum dolor sit amet, consectetur adipisicig elit, sed do eiusmod tempor incididunut labore et doloagna astum aliqua.</p>
<p class="intro-body abs" style="left:447px;top:589px">Uenim ad minim veniam, quis nostrud laboris nisi utaliquip ex ea commodoconsequat. Duisute irurdolor into reprehen-deritin voluptate velit esse cillum.</p>
<div class="more abs" style="left:302px;top:630px"><i><svg width="7" height="7" viewBox="0 0 7 7"><path d="M1 1 L3.5 3.5 L1 6 M3.5 1 L6 3.5 L3.5 6" stroke="#fff" fill="none"/></svg></i>read more</div>

<h2 class="section-title abs" style="left:303px;top:667px">Solutions Overview</h2>
<div class="solution abs" style="left:302px;top:702px"><h3>Property Development</h3><p>massasoluta nobis est eligendi omnis voluasassumenda est, omnis dolore-sereeledusempquibusdamet aurerum odes perferendis doloribus asperiores repellat dolore</p></div>
<div class="solution abs" style="left:512px;top:702px"><h3>Conveyancing</h3><p>massasoluta nobis est eligendi omnis voluasassumenda est, omnis dolore-sereeledusempquibusdamet aurerum odes perferendis doloribus asperiores repellat dolore</p></div>
<div class="more abs" style="left:302px;top:781px"><i><svg width="7" height="7" viewBox="0 0 7 7"><path d="M1 1 L3.5 3.5 L1 6 M3.5 1 L6 3.5 L3.5 6" stroke="#fff" fill="none"/></svg></i>read more</div>
<div class="more abs" style="left:512px;top:781px"><i><svg width="7" height="7" viewBox="0 0 7 7"><path d="M1 1 L3.5 3.5 L1 6 M3.5 1 L6 3.5 L3.5 6" stroke="#fff" fill="none"/></svg></i>read more</div>
<div class="solution abs" style="left:302px;top:818px"><h3>General Property Law</h3><p>massasoluta nobis est eligendi omnis voluasassumenda est, omnis dolore-sereeledusempquibusdamet aurerum odes perferendis doloribus asperiores repellat dolore</p></div>
<div class="solution abs" style="left:512px;top:818px"><h3>Strata &amp; Community Title</h3><p>massasoluta nobis est eligendi omnis voluasassumenda est, omnis dolore-sereeledusempquibusdamet aurerum odes perferendis doloribus asperiores repellat dolore</p></div>
<div class="more abs" style="left:302px;top:897px"><i><svg width="7" height="7" viewBox="0 0 7 7"><path d="M1 1 L3.5 3.5 L1 6 M3.5 1 L6 3.5 L3.5 6" stroke="#fff" fill="none"/></svg></i>read more</div>
<div class="more abs" style="left:512px;top:897px"><i><svg width="7" height="7" viewBox="0 0 7 7"><path d="M1 1 L3.5 3.5 L1 6 M3.5 1 L6 3.5 L3.5 6" stroke="#fff" fill="none"/></svg></i>read more</div>

<div class="contact-band"></div>
<footer class="site-footer">
  <h2 class="contact-title">Contact Me</h2>
  <p class="contact-text">Lorem ipsum dolor sit amet, consectetuer adipiscing elit. Praesent vestibulum m olestie lacus. Aenean nonummy<br>hendrerit mauris. Phasellus porta. Fusce suscipit varius mi. Lorem ipsum dolor sit amet, consectetuer adipiscing elit.<br>Praesent vestibulum molestie lacus. Morbi nunc odio, gravida at, cursus neca</p>
  <p class="contact-line" style="left:0;width:786px;text-align:center;top:110px">PO Box 412 Ashvale NSW 2150.</p>
  <p class="contact-line" style="left:220px;top:126px">Telephone: +02 9000 4821</p>
  <p class="contact-line" style="left:384px;top:126px">E-mail: enquiries@bramblewoodlegal.com.au</p>
  <div class="drop-btn">DROP ME A MASSAGE</div>
  <div class="footer-rule"></div>
  <p class="copyright">Copyright © 2015 - All Rights Reserved</p>
  <p class="disclaimer">Bramblewood Legal is a business name of Bramblewood Legal Pty Limited ACN 482 517 306, an incorporated legal practice regulated by the Legal Profession Act 2004. Liability limited by a scheme approved under the Professional Standards Legislation.</p>
  <div class="social" style="left:594px"><svg width="17" height="13" viewBox="0 0 17 13"><rect x="0.5" y="0.5" width="16" height="12" fill="#fff"/><path d="M0.5 0.5 L8.5 7 L16.5 0.5 M0.5 12.5 L6 6 M16.5 12.5 L11 6" stroke="#333" fill="none"/></svg></div>
  <div class="social" style="left:629px"><svg width="14" height="14"><circle cx="7" cy="7" r="6" fill="#fff"/></svg></div>
  <div class="social" style="left:663px"><svg width="14" height="14"><circle cx="7" cy="7" r="6" fill="#fff"/></svg></div>
  <div class="social" style="left:698px"><svg width="11" height="18" viewBox="0 0 11 18"><rect x="1" y="1" width="9" height="16" rx="1.5" fill="none" stroke="#fff" stroke-width="1.6"/><circle cx="5.5" cy="14" r="1" fill="#fff"/></svg></div>
</footer>

</body>
</html>
```